Larkfield Concrete Pumping

We need a brochure or a flyer to advertise our Concrete Pumping Business

Contact Information for Business Card

Same as the brochure with prices on the back

Font styles to use
Sans Serif

Requirements
Must have
• Prices
Nice to have
• Pictures of the trucks, prices.

```html
<!DOCTYPE html>
<html lang="en">
<head>
<meta charset="utf-8">
<title>Larkfield Concrete Pumping — Flyer and Business Cards</title>
<link href="https://fonts.googleapis.com/css2?family=Montserrat:wght@500;700;800&display=swap" rel="stylesheet">
<style>
  :root {
    --navy: #22306a;
    --paper: #ffffff;
    --rule: #d5d8e4;
    --muted: #5a6390;
    --backdrop-top: #ececee;
    --backdrop-bottom: #dcdce0;
    --truck-red: #b4233a;
    --truck-blue: #3d88c8;
    --truck-cream: #e3dcc4;
  }
  * { margin: 0; padding: 0; box-sizing: border-box; }
  html, body { width: 1200px; height: 2452px; overflow: hidden; }
  body {
    position: relative;
    background: linear-gradient(180deg, var(--backdrop-top), var(--backdrop-bottom));
    font-family: "Montserrat", Arial, sans-serif;
    color: var(--navy);
  }
  .wordmark { font-weight: 800; letter-spacing: -0.01em; }

  /* Flyer sheet */
  .flyer {
    position: absolute; left: 179px; top: 684px;
    width: 842px; height: 1084px;
    background: var(--paper);
  }
  .flyer-band {
    position: absolute; left: 0; top: 0; width: 100%; height: 148px;
    background: var(--navy); color: var(--paper);
  }
  .flyer .wordmark {
    position: absolute; left: 69px; top: 68px;
    font-size: 22px; line-height: 21px;
  }
  .flyer-contact {
    position: absolute; right: 70px; top: 91px;
    font-size: 15px; font-weight: 500; line-height: 21px;
    text-align: right; letter-spacing: 0.02em;
  }
  .flyer-intro {
    position: absolute; left: 69px; right: 70px; top: 196px;
  }
  .flyer-title { font-size: 34px; font-weight: 800; line-height: 40px; }
  .flyer-lede {
    margin-top: 12px; font-size: 16px; font-weight: 500; line-height: 24px;
    color: var(--muted); max-width: 560px;
  }

  .price-list {
    position: absolute; left: 69px; right: 70px; top: 762px;
  }
  .price-heading {
    font-size: 18px; font-weight: 800; letter-spacing: 0.08em;
    text-transform: uppercase; padding-bottom: 12px;
    border-bottom: 3px solid var(--navy);
  }
  .price-table { width: 100%; border-collapse: collapse; }
  .price-table td {
    padding: 13px 0; font-size: 17px; font-weight: 500;
    border-bottom: 1px solid var(--rule);
  }
  .price-table .price { text-align: right; font-weight: 800; }
  .price-note {
    margin-top: 14px; font-size: 14px; font-weight: 500; color: var(--muted);
  }

  /* Business cards */
  .card {
    position: absolute; top: 1111px;
    width: 475px; height: 285px;
    background: var(--paper);
    box-shadow: 0 1px 3px rgba(0,0,0,0.08);
    overflow: hidden;
  }
  .card-front { left: 67px; }
  .card-front .wordmark {
    position: absolute; left: 40px; top: 39px;
    font-size: 28px; line-height: 27px;
  }
  .card-front-band {
    position: absolute; left: 0; top: 175px; width: 100%; height: 110px;
    background: var(--navy); color: var(--paper);
    display: flex; align-items: center; gap: 24px;
    padding-left: 52px;
    font-size: 15px; font-weight: 500; letter-spacing: 0.02em;
  }

  .card-back { left: 659px; }
  .card-back-panel {
    position: absolute; left: 238px; top: 0; width: 237px; height: 100%;
    background: var(--navy);
  }
  .card-back .wordmark {
    position: absolute; left: 41px; top: 39px;
    font-size: 18px; line-height: 17px;
  }
  .card-back-contact {
    position: absolute; left: 41px; top: 203px;
    font-size: 13px; font-weight: 500; line-height: 19px;
  }
  .truck-photo { position: absolute; left: 169px; top: 49px; width: 280px; height: 193px; }
</style>
</head>
<body>
  <section class="flyer">
    <header class="flyer-band">
      <div class="wordmark">Larkfield<br>Concrete<br>Pumping</div>
      <div class="flyer-contact">phone : (555) 201-4870<br>fax : (555) 201-4871</div>
    </header>

    <div class="flyer-intro">
      <h1 class="flyer-title">Concrete Pumping Rates</h1>
      <p class="flyer-lede">Boom and line pumps for residential and commercial pours, with an experienced operator on every job.</p>
    </div>

    <div class="price-list">
      <h2 class="price-heading">Prices</h2>
      <table class="price-table">
        <tr><td>32 m boom pump</td><td class="price">$165 / hr</td></tr>
        <tr><td>38 m boom pump</td><td class="price">$185 / hr</td></tr>
        <tr><td>47 m boom pump</td><td class="price">$215 / hr</td></tr>
        <tr><td>Line pump</td><td class="price">$135 / hr</td></tr>
        <tr><td>Per cubic yard pumped</td><td class="price">$4.50</td></tr>
      </table>
      <p class="price-note">Four hour minimum on all pumps. Call (555) 201-4870 to book.</p>
    </div>
  </section>

  <section class="card card-front">
    <div class="wordmark">Larkfield<br>Concrete<br>Pumping</div>
    <div class="card-front-band">
      <span>phone: (555) 201-4870</span>
      <span>fax (555) 201-4871</span>
    </div>
  </section>

  <section class="card card-back">
    <div class="card-back-panel"></div>
    <div class="wordmark">Larkfield<br>Concrete<br>Pumping</div>
    <div class="card-back-contact">fx(555) 201-4871<br>ph(555) 201-4870</div>
    <svg class="truck-photo" viewBox="0 0 280 193" role="img" aria-label="Photo of two concrete pump trucks, a red boom truck above a blue and cream boom truck">
      <defs>
        <linearGradient id="upper-truck" x1="0" y1="0" x2="1" y2="0">
          <stop offset="0" stop-color="#e3dcc4"/>
          <stop offset="0.3" stop-color="#b4233a"/>
          <stop offset="1" stop-color="#b4233a"/>
        </linearGradient>
        <linearGradient id="lower-truck" x1="0" y1="0" x2="0" y2="1">
          <stop offset="0" stop-color="#3d88c8"/>
          <stop offset="1" stop-color="#e3dcc4"/>
        </linearGradient>
      </defs>
      <rect x="0" y="0" width="280" height="90" rx="6" fill="url(#upper-truck)" opacity="0.9"/>
      <rect x="0" y="100" width="280" height="93" rx="6" fill="url(#lower-truck)" opacity="0.9"/>
    </svg>
  </section>
</body>
</html>
```